Circular Wedding Menu Design - Adobe Illustrator

I am looking for a design for circular wedding menus. these will be 7 inches.I'm providing a template from the printer, AI files of our wedding invitation, and the menu items.

The paper our invitations were printed on was a sandy beige color. please make the background for this the same color. It will be put ontop of a white plate with ivory tablecloth and cappucino covered napkins.

IMPORTANT - We aren't committed to a specific design so feel free to use whatever you like, but we definitely want the cow, fish, and carrot images from our rsvp to be used for the entrees in the menu.

IMPORTANT - must be in Adobe illustrator format

for inspiration:
http://cdn.plumbridalpages.example/wp-content/uploads/2012/10/harvel-styled-19.jpg

http://www.pictofind.example/imgres?imgurl=http%3A%2F%2Fwww.velvetknotstudio.example%2Fblog%2Fwp-content%2Fuploads%2F2013%2F07%2FRound-Menu-Wedding-Place-Setting.jpg&imgrefurl=http%3A%2F%2Fwww.velvetknotstudio.example%2Fblog%2Finspiration%2Fsimply-lovely-wedding-menu-place-settings%2F&h=815&w=600&zoom=1&page=1&start=0&ndsp=30

https://thumbs3.pictofind.example/images?q=tbn:Xk4mPq7RtL2vNw9HbYc3JdZs8FgQe1Ua

https://thumbs3.pictofind.example/images?q=tbn:Rb6wLn2TqZ8kVe4MhXs1PcYj9DuGa3Wo

https://thumbs2.pictofind.example/images?q=tbn:Hn5cWq8JtM3sLz7PxVb2KeRd6YgFo1Ni

```html
<!DOCTYPE html>
<html lang="en">
<head>
<meta charset="utf-8">
<title>Wedding Menu</title>
<link href="https://fonts.googleapis.com/css2?family=Aleo:wght@300;400;700&display=swap" rel="stylesheet">
<style>
  :root {
    --frame: #2b2b2b;
    --page: #ffffff;
    --sand: #dbcfb4;
    --sand-deep: #cfc3a8;
    --gold: #b08a28;
    --ink: #85837f;
  }
  html, body {
    margin: 0;
    padding: 0;
    width: 1200px;
    height: 1000px;
    overflow: hidden;
    background: var(--page);
  }
  .canvas {
    position: relative;
    width: 1200px;
    height: 1000px;
    overflow: hidden;
    font-family: "Aleo", Georgia, serif;
  }
  .frame {
    position: absolute;
    left: 20px;
    top: 17px;
    width: 1150px;
    height: 950px;
    border: 5px solid var(--frame);
    background: var(--page);
  }
  .menu-disc {
    position: absolute;
    left: 164px;
    top: 60px;
    width: 880px;
    height: 880px;
    border-radius: 50%;
    background: var(--sand);
    overflow: hidden;
  }
  .vine-art {
    position: absolute;
    left: 40px;
    top: 290px;
    width: 720px;
    height: 170px;
    border-radius: 50%;
    transform: rotate(-38deg);
    transform-origin: center;
    background: radial-gradient(ellipse at center, rgba(190,182,165,0.45) 0%, rgba(190,182,165,0.2) 55%, rgba(190,182,165,0) 75%);
  }
  .menu-title {
    position: absolute;
    left: 0;
    width: 1200px;
    top: 212px;
    margin: 0;
    text-align: center;
    font-weight: 400;
    font-size: 84px;
    line-height: 100px;
    letter-spacing: 1px;
    color: var(--gold);
  }
  .course-heading {
    position: absolute;
    margin: 0;
    font-weight: 700;
    font-size: 22px;
    line-height: 26px;
    color: var(--gold);
  }
  .course-text {
    position: absolute;
    margin: 0;
    font-weight: 400;
    font-size: 17px;
    line-height: 23px;
    color: var(--ink);
  }
  .align-right { text-align: right; }
  .salad-heading { right: 267px; top: 333px; }
  .salad-text { right: 267px; top: 359px; width: 420px; }
  .entree-heading { left: 368px; top: 467px; }
  .entree-beef { left: 368px; top: 491px; }
  .entree-fish { left: 368px; top: 563px; }
  .entree-veg { left: 368px; top: 634px; }
  .cake-heading { right: 336px; top: 728px; }
  .cake-text { right: 336px; top: 754px; }
  .entree-icon {
    position: absolute;
    left: 306px;
    width: 40px;
    height: 34px;
    border-radius: 8px;
    background: var(--gold);
    opacity: 0.85;
  }
  .icon-beef { top: 499px; }
  .icon-fish { top: 571px; }
  .icon-veg { top: 641px; left: 310px; width: 32px; }
</style>
</head>
<body>
<div class="canvas">
  <div class="frame"></div>
  <div class="menu-disc">
    <div class="vine-art" role="img" aria-label="Faint botanical vine with leaves sweeping across the menu"></div>
  </div>

  <h1 class="menu-title">MENU</h1>

  <h2 class="course-heading salad-heading">Salad</h2>
  <p class="course-text align-right salad-text">Grilled Watermelon &amp; Fig Salad: Gem Lettuces,<br>Watermelon, Figs, Toasted Hazelnuts, Balsamic<br>Reduction, Honey-Orange Dressing</p>

  <h2 class="course-heading entree-heading">Entrée</h2>
  <div class="entree-icon icon-beef" role="img" aria-label="Cow icon marking the beef entrée"></div>
  <p class="course-text entree-beef">Roasted Filet Mignon, Wild Mushrooms, Garlic Mashed<br>Potatoes, Asparagus with Red Wine Sauce</p>
  <div class="entree-icon icon-fish" role="img" aria-label="Fish icon marking the fish entrée"></div>
  <p class="course-text entree-fish">Porcini Crusted Halibut, Lemon-Herb Potatoes,<br>Black Kale, Early Girl Tomatoes</p>
  <div class="entree-icon icon-veg" role="img" aria-label="Carrot icon marking the vegetarian entrée"></div>
  <p class="course-text entree-veg">Artichoke Agnolotti, Wild Mushrooms, Baby Arugula,<br>Goat Cheese, White Wine Sauce, Micro herbs</p>

  <h2 class="course-heading align-right cake-heading">Wedding Cake</h2>
  <p class="course-text align-right cake-text">Delicate Butter Pecan With Fresh Raspberry Mouse</p>
</div>
</body>
</html>
```